L.M.T. Penrow

I am an indie author and already have a Facebook page. However, I would like it to be more professional and look less like a private Facebook page.

```html
<!DOCTYPE html>
<html lang="en">
<head>
<meta charset="utf-8">
<title>L.M.T. Penrow – Cover Banner</title>
<link rel="stylesheet" href="https://fonts.googleapis.com/css2?family=Oswald:wght@500&family=Mr+Dafoe&display=swap">
<style>
  :root {
    --page-bg: #e9ebee;
    --blue-deep: #062b55;
    --blue-mid: #0f4a85;
    --blue-light: #2a6fb0;
    --gold: #f1dc7a;
    --gold-bright: #f6e27f;
    --label-dark: #1c1c1c;
    --label-light: #4a4a4a;
    --white: #ffffff;
  }
  html, body {
    margin: 0;
    padding: 0;
    width: 1021px;
    height: 1200px;
    overflow: hidden;
    background: var(--page-bg);
  }
  .stage {
    position: relative;
    width: 1021px;
    height: 1200px;
    display: flex;
    align-items: center;
    justify-content: center;
  }
  .cover-banner {
    display: block;
    width: 1021px;
    height: 385px;
    box-shadow: 4px 4px 10px rgba(0,0,0,0.35);
  }
  .author-name, .author-role {
    font-family: "Oswald", "Arial Narrow", sans-serif;
    font-weight: 500;
    fill: var(--gold);
  }
  .book-title {
    font-family: "Mr Dafoe", cursive;
    fill: var(--gold-bright);
  }
  .tagline {
    font-family: "Oswald", "Arial Narrow", sans-serif;
    font-weight: 500;
    fill: var(--white);
  }
  .store-name {
    font-family: "Oswald", "Arial Narrow", sans-serif;
    font-weight: 500;
    fill: var(--white);
  }
</style>
</head>
<body>
<main class="stage">
  <svg class="cover-banner" viewBox="0 0 1060 400" xmlns="http://www.w3.org/2000/svg">
    <defs>
      <radialGradient id="sky" cx="0.45" cy="0.35" r="0.8">
        <stop offset="0" stop-color="var(--blue-light)"/>
        <stop offset="0.55" stop-color="var(--blue-mid)"/>
        <stop offset="1" stop-color="var(--blue-deep)"/>
      </radialGradient>
      <linearGradient id="label" x1="0" y1="0" x2="1" y2="1">
        <stop offset="0" stop-color="var(--label-light)"/>
        <stop offset="0.6" stop-color="var(--label-dark)"/>
        <stop offset="1" stop-color="#0e0e0e"/>
      </linearGradient>
      <linearGradient id="books" x1="0" y1="0" x2="1" y2="1">
        <stop offset="0" stop-color="#3a2a26"/>
        <stop offset="0.4" stop-color="#b8562a"/>
        <stop offset="0.7" stop-color="#2a2a2e"/>
        <stop offset="1" stop-color="#d8d6d0"/>
      </linearGradient>
    </defs>

    <rect class="banner-bg" width="1060" height="400" fill="url(#sky)"/>

    <g class="author-label">
      <polygon points="60,112 360,118 326,280 56,262" fill="var(--gold)"/>
      <polygon points="300,130 386,126 346,262 280,270" fill="var(--gold)"/>
      <polygon points="70,108 372,100 340,284 22,236" fill="none" stroke="#cfe0f2" stroke-width="1.2"/>
      <polygon points="74,110 360,128 336,278 38,246" fill="url(#label)"/>
      <text class="author-name" x="203" y="178" font-size="31" text-anchor="middle">L.M.T. Penrow</text>
      <text class="author-role" x="203" y="216" font-size="31" text-anchor="middle">Author Of Suspense</text>
    </g>

    <rect class="book-display" x="385" y="72" width="375" height="262" rx="6" fill="url(#books)" opacity="0.9" role="img" aria-label="Paperback, hardback, e-reader and phone showing the novel Strata cover"/>

    <g class="book-promo">
      <text class="book-title" x="895" y="158" font-size="112" text-anchor="middle">Strata</text>
      <text class="tagline" x="786" y="232" font-size="34">Letting Celeste</text>
      <text class="tagline" x="786" y="269" font-size="34">into his house is</text>
      <text class="tagline" x="786" y="307" font-size="34">a big mistake…</text>
    </g>

    <g class="store-list">
      <rect x="788" y="330" width="9" height="9" fill="var(--gold)"/>
      <text class="store-name" x="801" y="339" font-size="12">Tomo</text>
      <rect x="839" y="330" width="9" height="9" fill="var(--gold)"/>
      <text class="store-name" x="852" y="339" font-size="12">Arvida</text>
      <rect x="896" y="330" width="9" height="9" fill="var(--gold)"/>
      <text class="store-name" x="909" y="339" font-size="12">Pageleaf</text>
      <rect x="962" y="330" width="9" height="9" fill="var(--gold)"/>
      <text class="store-name" x="975" y="339" font-size="12">Cranny</text>
    </g>
  </svg>
</main>
</body>
</html>
```